yourSmileCare Brookvale Business Card

Please design a two sided business card that is Elegant and Professional
Add subtle elegant patterns to suit Spot UV printing/ or raised printing

Name: Dr Marcus T. Fenwick
Qualification: BDSc (QLD)
Title: Dental Surgeon, Clinical Director
Company: yourSmileCare Brookvale
Phone: (02) 7593 2268
Address: Shop 7/18-20 Lindon Ave Brookvale 2097
email: info@yoursmilecarebrookvale.com.au
Facebook: facebook.com/yoursmilecarebrookvale

Motto:
Quality dentistry you can trust

Description of services (not compulsory):
Preventative Dentistry | General Dentistry
Cosmetic Dentistry | Teeth Whitening
Crown and Bridge | Root Canal Therapy
Veneers | Clearvono | Orthodontics
Emergency Dental Care | After Hours

Personalised Treatment Plans
Transparent Fees

Please make sure card is elegant and professional

Target Market(s)

general population, patients,
Dental sales companies, other professions

Industry/Entity Type

Dental Clinic

Contact Information for Business Card

Name: Dr Marcus T. Fenwick
Qualification: BDSc (QLD)
Phone: (02) 7593 2268
Address: Shop 7/18-20 Lindon Ave Brookvale

Motto:

Description of services (not compulsory)

Transparent Fees

Image of dental surgery optional

Please make sure card is elegant and profession

Requirements
Must have
• Logo
• Name, Title (next to name), Business
• Phone, address, facbeook
• Must have stylish design to suit SPOT UV reflective printing
Nice to have
• Subtle elegant patterns which will have Spot UV on them when printed
• Colours to match logo colour
• Description of services
Should not have
• Small fonts that are hard to read
• DO NOT PUT IMAGES OF DENTAL INSTRUMENTS OR TEETH PLEASE

```html
<!DOCTYPE html>
<html lang="en">
<head>
<meta charset="utf-8">
<title>yourSmileCare Brookvale – Business Card</title>
<link href="https://fonts.googleapis.com/css2?family=Arimo:ital,wght@0,400;0,700;1,700&family=Alfa+Slab+One&display=swap" rel="stylesheet">
<style>
  :root {
    --paper: #ffffff;
    --backdrop: #fbb7cc;
    --mint: #38e38a;
    --slate: #687a80;
    --ink-grey: #6b7575;
    --lime: #7dfc12;
    --white: #ffffff;
  }
  * { box-sizing: border-box; margin: 0; padding: 0; }
  html, body {
    width: 1200px; height: 1200px; overflow: hidden;
    background: var(--paper);
    font-family: "Arimo", Arial, sans-serif;
  }
  .backdrop {
    position: absolute; left: 0; top: 70px; width: 1152px; height: 1130px;
    background: var(--backdrop);
  }
  .card {
    position: absolute; left: 304px; width: 594px; height: 376px;
    box-shadow: 0 8px 22px rgba(120, 60, 80, 0.25);
  }
  /* Front */
  .card-front { top: 247px; background: var(--mint); }
  .brand {
    position: absolute; left: 0; right: 0; top: 345px; margin-top: -247px;
    display: flex; justify-content: center; align-items: center; gap: 10px;
  }
  .brand-dot { width: 14px; height: 14px; border-radius: 50%; background: var(--ink-grey); }
  .brand-name { font-size: 30px; font-weight: 400; color: var(--ink-grey); letter-spacing: 0.2px; }
  .motto {
    position: absolute; left: 0; right: 0; top: 189px;
    text-align: center; font-size: 22px; color: var(--ink-grey);
  }
  .name-rule {
    position: absolute; left: 176px; width: 242px; height: 1px; background: var(--lime);
  }
  .name-rule.top { top: 258px; }
  .name-rule.bottom { top: 300px; }
  .front-name {
    position: absolute; left: 0; right: 0; top: 266px;
    text-align: center; font-size: 24px; font-weight: 700; font-style: italic; color: var(--ink-grey);
  }
  .front-phone {
    position: absolute; left: 0; right: 0; top: 318px;
    display: flex; justify-content: center; align-items: center; gap: 14px;
    font-size: 35px; color: var(--ink-grey);
  }
  .front-phone svg { width: 30px; height: 30px; }
  /* Back */
  .card-back { top: 669px; background: var(--slate); }
  .mark-area {
    position: absolute; left: 446px; top: 23px; width: 116px; height: 100px;
    border-radius: 40px 40px 30px 30px;
    background: linear-gradient(160deg, var(--lime) 0%, var(--white) 45%);
  }
  .back-name-row {
    position: absolute; left: 0; right: 0; top: 128px;
    display: flex; justify-content: center; align-items: center; gap: 16px;
  }
  .tools-area { width: 26px; height: 44px; background: linear-gradient(90deg, var(--white) 0 30%, transparent 30% 65%, var(--white) 65%); opacity: 0.9; }
  .back-name { font-family: "Alfa Slab One", Georgia, serif; font-size: 33px; color: var(--white); }
  .title-band {
    position: absolute; left: 0; right: 0; top: 185px; height: 45px;
    background: var(--lime);
    display: flex; justify-content: center; align-items: center;
    font-size: 27px; font-weight: 700; font-style: italic; color: var(--white);
  }
  .contact-list { position: absolute; left: 116px; top: 275px; list-style: none; }
  .contact-list li {
    display: flex; align-items: center; gap: 12px; height: 32.5px;
    font-size: 18px; font-weight: 700; color: var(--lime);
  }
  .contact-icon { width: 30px; display: flex; justify-content: center; }
  .social-square { width: 20px; height: 20px; background: var(--white); }
</style>
</head>
<body>
  <div class="backdrop"></div>

  <section class="card card-front">
    <div class="brand" style="top:98px;margin-top:0">
      <span class="brand-dot"></span>
      <span class="brand-name">yourSmileCare Brookvale</span>
    </div>
    <p class="motto">Quality Dentistry You Can Trust</p>
    <div class="name-rule top"></div>
    <p class="front-name">Dr. Marcus T. Fenwick</p>
    <div class="name-rule bottom"></div>
    <div class="front-phone">
      <svg viewBox="0 0 24 24" fill="none" stroke="#ffffff" stroke-width="1.4" aria-hidden="true">
        <path d="M5 3l3 0 2 5-2 1.5c1 2.5 3 4.5 5.5 5.5L15 13l5 2v3c0 1-1 2-2 2C10 20 4 14 4 6c0-1 0-3 1-3z"/>
      </svg>
      <span>(02) 7593 2268</span>
    </div>
  </section>

  <section class="card card-back">
    <div class="mark-area" role="img" aria-label="Clinic emblem area"></div>
    <div class="back-name-row">
      <div class="tools-area" role="img" aria-label="Small clinical emblem"></div>
      <h1 class="back-name">DR. Marcus T. Fenwick</h1>
    </div>
    <div class="title-band">Dental Surgeon ,&nbsp; Clinical Director</div>
    <ul class="contact-list">
      <li><span class="contact-icon"><span class="social-square"></span></span>facebook.com/yoursmilecarebrookvale</li>
      <li><span class="contact-icon">
        <svg width="20" height="26" viewBox="0 0 20 26" fill="none" stroke="#ffffff" stroke-width="1.6" aria-hidden="true">
          <path d="M10 24C4 16 2 12 2 9a8 8 0 0116 0c0 3-2 7-8 15z"/><circle cx="10" cy="9" r="3"/>
        </svg></span>Shop 7/18-20 Lindon Ave Brookvale</li>
      <li><span class="contact-icon">
        <svg width="30" height="22" viewBox="0 0 30 22" fill="none" stroke="#ffffff" stroke-width="1.6" aria-hidden="true">
          <rect x="1" y="1" width="28" height="20"/><path d="M1 1l14 11L29 1M1 21l10-10M29 21L19 11"/>
        </svg></span>info@yoursmilecarebrookvale.com.au</li>
    </ul>
  </section>
</body>
</html>
```